A stationary and business card desgn for a podiatry clinic

i require a stationary design for letter heads, envelopes, buisness cards.

it is for a new podiatry practise within a medical centre, that deals with all lower limb pathology and injury and foot related problems.

the colour scheme for my exisiting logo is orange blue and white. colours provided below.
i would like a white background for the buisness card.

the final design should portray health and wellbeing in a professional manner that still looks modern but sophisticated.

male and female, off all ethinical backgrounds aged between 30-80 years

Medical

• letter head.
need to include all contact details mentioned below.
need to also include ABN 53208741196

i prefer the logo on the top left hand corner and the contact info on the right. the address can be written in a sentence like form as the footer.

Business card
Front:

include logo provided.

clinic details on the front of the card.

Carla Westbrook
B.Pod

P: 8391 4460
F: 8391 4478
M: 0437 612 809
E: carla@velmora.com.au
W: www.velmora.com.au

(may use icons to indicate contact type)

on back

Appointments:

lines to write dates, time etc.
(3-4 of these)
and a small photo of just the foot from the logo in coloured watermark.

Address:
Larkvale Medical Centre
41 Tambrell Street
Carrowdale SA 5117
(this location infomation could be in smaller font at the bottom of the buisness card under a line, running in a sentence like fashion) or in the bottom left or right hand corner in a paragraph like you would write it on an envelope

however if you think a different lay out at the back will look better by all means i just need to have room for the appointment even if it is just lines/ space.

i also prefer square cards not rounded corners.

thanks
• plain texts such as times new roman and arial

```html
<!DOCTYPE html>
<html lang="en">
<head>
<meta charset="utf-8">
<title>Velmora Podiatry – Appointment Card (Back)</title>
<link rel="stylesheet" href="https://fonts.googleapis.com/css2?family=Source+Sans+3:wght@400;600;700&display=swap">
<style>
  :root {
    --backdrop: #b8922f;
    --card-white: #ffffff;
    --brand-orange: #e8692a;
    --band-orange-light: #ea6a2c;
    --band-orange-dark: #c24a1b;
    --rule-dark: #3a3a3a;
    --mark-blue: #a9aedb;
    --band-text: #ffffff;
  }

  * { box-sizing: border-box; margin: 0; padding: 0; }

  html, body {
    width: 1200px;
    height: 738px;
    overflow: hidden;
  }

  body {
    background: var(--backdrop);
    font-family: "Source Sans 3", Arial, sans-serif;
    position: relative;
  }

  .card-back {
    position: absolute;
    left: 38px;
    top: 69px;
    width: 1058px;
    height: 605px;
    background: var(--card-white);
    overflow: hidden;
  }

  .appointments-title {
    position: absolute;
    left: 54px;
    top: 52px;
    font-size: 32px;
    font-weight: 700;
    line-height: 1.2;
    color: var(--brand-orange);
    letter-spacing: 0.2px;
  }

  .appointment-lines {
    position: absolute;
    left: 54px;
    top: 0;
    width: 608px;
    list-style: none;
  }

  .appointment-line {
    position: absolute;
    left: 0;
    width: 608px;
    height: 0;
    border-top: 2px dotted var(--rule-dark);
  }

  .appointment-line:nth-child(1) { top: 182px; }
  .appointment-line:nth-child(2) { top: 251px; }
  .appointment-line:nth-child(3) { top: 319px; }
  .appointment-line:nth-child(4) { top: 389px; }

  .brand-watermark {
    position: absolute;
    left: 690px;
    top: 250px;
    width: 320px;
    display: flex;
    align-items: center;
    justify-content: center;
    gap: 14px;
  }

  .brand-watermark__dot {
    width: 26px;
    height: 26px;
    border-radius: 50%;
    background: var(--mark-blue);
    flex: none;
  }

  .brand-watermark__name {
    font-size: 34px;
    font-weight: 600;
    color: var(--mark-blue);
    white-space: nowrap;
  }

  .address-band {
    position: absolute;
    left: 0;
    bottom: 0;
    width: 100%;
    height: 104px;
    background: linear-gradient(90deg, var(--band-orange-dark) 0%, var(--band-orange-light) 50%, var(--band-orange-dark) 100%);
    display: flex;
    align-items: center;
    justify-content: center;
  }

  .address-line {
    font-size: 25px;
    font-weight: 400;
    color: var(--band-text);
    display: flex;
    align-items: center;
    gap: 10px;
    white-space: nowrap;
  }

  .address-sep {
    width: 12px;
    height: 12px;
    border-radius: 50%;
    background: var(--band-text);
    display: inline-block;
  }
</style>
</head>
<body>
  <section class="card-back" aria-label="Appointment card">
    <h1 class="appointments-title">Appointments:</h1>

    <ul class="appointment-lines" aria-label="Appointment lines">
      <li class="appointment-line"></li>
      <li class="appointment-line"></li>
      <li class="appointment-line"></li>
      <li class="appointment-line"></li>
    </ul>

    <div class="brand-watermark">
      <span class="brand-watermark__dot"></span>
      <span class="brand-watermark__name">Velmora Podiatry</span>
    </div>

    <footer class="address-band">
      <p class="address-line">
        <span>Larkvale Medical Centre</span>
        <span class="address-sep"></span>
        <span>41 Tambrell Street</span>
        <span class="address-sep"></span>
        <span>Carrowdale SA 5117</span>
      </p>
    </footer>
  </section>
</body>
</html>
```